Brisket Dwelling Review is a leading provider of residential appraisal and home inspection products in S

I need a business card/logo designed that obviously describes my business. We are a residential appraisal and home inspection company in Springfield, MO. We offer residential appraisals, home inspection, pest inspection and radon gas measurement. We have been in business for 18 years and hold state certified residential appraisal licenses and VORMEL certified home inspection licenses. I have a logo that I really like and will attach, but would be open to new suggestions. I like more modern designs than traditional and would like a two sided card with our services, licenses and qualifications on the back.

```html
<!DOCTYPE html>
<html lang="en">
<head>
<meta charset="utf-8">
<title>Brisket Dwelling Review – Business Card</title>
<link rel="stylesheet" href="https://fonts.googleapis.com/css2?family=Source+Sans+3:wght@400;600&display=swap">
<style>
  :root {
    --page-bg: #d6d6d6;
    --card-light: #f2f2f2;
    --card-light-edge: #d4d4d4;
    --brand-brown: #8a6842;
    --dark-brown: #2a1a10;
    --dark-brown-2: #3d2a1e;
    --brand-orange: #ef9a33;
    --ink: #1e1e1e;
    --white: #f4f4f4;
  }
  html, body {
    margin: 0;
    padding: 0;
    width: 1189px;
    height: 1200px;
    overflow: hidden;
    background: var(--page-bg);
  }
  .canvas {
    position: relative;
    width: 1189px;
    height: 1200px;
  }
  .card {
    position: absolute;
    left: 140px;
    width: 917px;
    height: 524px;
    box-shadow: 0 6px 14px rgba(0,0,0,0.35);
  }
  .card--front { top: 45px; }
  .card--back { top: 624px; }
  .card svg { display: block; width: 917px; height: 524px; }
  .type { font-family: "Source Sans 3", sans-serif; }
  .brand-name { font-weight: 600; font-size: 56px; }
  .brand-name--front { fill: var(--brand-brown); }
  .brand-name--back { fill: var(--white); }
  .contact { font-size: 30px; fill: var(--ink); font-weight: 400; }
  .services-title { font-size: 72px; fill: var(--white); font-weight: 400; }
  .service { font-size: 31px; fill: var(--white); font-weight: 400; }
  .icon-box { fill: var(--brand-orange); }
  .icon-glyph { fill: none; stroke: #fff; stroke-width: 2; stroke-linejoin: round; }
  .tick { fill: none; stroke: var(--white); stroke-width: 5; stroke-linecap: round; stroke-linejoin: round; }
</style>
</head>
<body>
<div class="canvas">

  <!-- Front of card -->
  <div class="card card--front">
    <svg viewBox="0 0 1123 642" class="type" aria-label="Front of business card">
      <defs>
        <radialGradient id="frontGlow" cx="0.5" cy="0.45" r="0.75">
          <stop offset="0" stop-color="#ffffff"/>
          <stop offset="1" stop-color="#d2d2d2"/>
        </radialGradient>
        <linearGradient id="orangeFill" x1="0" y1="1" x2="1" y2="0">
          <stop offset="0" stop-color="#f08a1c"/>
          <stop offset="1" stop-color="#f0a84a"/>
        </linearGradient>
      </defs>
      <rect width="1123" height="642" fill="url(#frontGlow)"/>

      <text class="brand-name brand-name--front" x="563" y="262" text-anchor="middle">Brisket Dwelling Review</text>

      <g class="contact-phones">
        <text class="contact" x="355" y="384" text-anchor="end">417-555-0142</text>
        <text class="contact" x="355" y="426" text-anchor="end">417-555-0187</text>
        <text class="contact" x="355" y="469" text-anchor="end">417-555-0163</text>

        <rect class="icon-box" x="384" y="355" width="30" height="30"/>
        <path class="icon-glyph" d="M393 361 l4 0 l2 6 l-3 2 q2 5 6 7 l2 -3 l6 2 l0 4 q-12 1 -17 -18 z"/>
        <rect class="icon-box" x="384" y="397" width="30" height="30"/>
        <rect class="icon-glyph" x="393" y="401" width="12" height="22" rx="1"/>
        <rect class="icon-glyph" x="396" y="405" width="6" height="6"/>
        <rect class="icon-box" x="384" y="440" width="30" height="30"/>
        <rect class="icon-glyph" x="389" y="450" width="20" height="11"/>
        <rect class="icon-glyph" x="393" y="444" width="12" height="6"/>
        <rect class="icon-glyph" x="393" y="458" width="12" height="7"/>
      </g>

      <line x1="444" y1="330" x2="444" y2="490" stroke="var(--brand-orange)" stroke-width="3"/>

      <g class="contact-details">
        <rect class="icon-box" x="480" y="355" width="30" height="30"/>
        <rect class="icon-glyph" x="486" y="362" width="18" height="14"/>
        <path class="icon-glyph" d="M486 362 l9 8 l9 -8"/>
        <rect class="icon-box" x="480" y="396" width="30" height="30"/>
        <path d="M495 401 l10 9 h-3 v9 h-5 v-5 h-4 v5 h-5 v-9 h-3 z" fill="#fff"/>

        <text class="contact" x="540" y="378">info@brisketdwellingreview.com</text>
        <text class="contact" x="540" y="419">Brisket Dwelling Review</text>
        <text class="contact" x="540" y="461">1482 W Larchmont Road; Suite C</text>
        <text class="contact" x="540" y="501">Springfield, MO  65810</text>
      </g>

      <path d="M470 642 Q880 610 1123 398 L1123 642 Z" fill="url(#orangeFill)"/>
      <path d="M0 572 Q640 650 1123 378 L1123 392 Q660 690 0 628 Z" fill="var(--dark-brown)"/>
    </svg>
  </div>

  <!-- Back of card -->
  <div class="card card--back">
    <svg viewBox="0 0 1123 642" class="type" aria-label="Back of business card">
      <defs>
        <linearGradient id="backFill" x1="0" y1="0" x2="1" y2="1">
          <stop offset="0" stop-color="#2a1a10"/>
          <stop offset="0.5" stop-color="#3d2a1e"/>
          <stop offset="1" stop-color="#28180e"/>
        </linearGradient>
      </defs>
      <rect width="1123" height="642" fill="url(#backFill)"/>

      <text class="brand-name brand-name--back" x="778" y="228" text-anchor="middle">Brisket Dwelling Review</text>

      <text class="services-title" x="80" y="323">Services</text>

      <g class="services-left">
        <path class="tick" d="M87 372 l7 8 l13 -19"/>
        <path class="tick" d="M87 410 l7 8 l13 -19"/>
        <path class="tick" d="M87 452 l7 8 l13 -19"/>
        <path class="tick" d="M87 493 l7 8 l13 -19"/>
        <path class="tick" d="M87 534 l7 8 l13 -19"/>
        <path class="tick" d="M87 577 l7 8 l13 -19"/>
        <text class="service" x="141" y="382">home inspection</text>
        <text class="service" x="141" y="420">property inspection</text>
        <text class="service" x="141" y="462">residential appraisal</text>
        <text class="service" x="141" y="503">termite inspection</text>
        <text class="service" x="141" y="544">radon gas measurement</text>
        <text class="service" x="141" y="587">pre purchase inspection</text>
      </g>

      <g class="services-right">
        <path class="tick" d="M641 410 l7 8 l13 -19"/>
        <path class="tick" d="M641 452 l7 8 l13 -19"/>
        <path class="tick" d="M641 493 l7 8 l13 -19"/>
        <path class="tick" d="M641 534 l7 8 l13 -19"/>
        <path class="tick" d="M641 577 l7 8 l13 -19"/>
        <text class="service" x="723" y="420">thermal imaging</text>
        <text class="service" x="723" y="462">mechanical inspection</text>
        <text class="service" x="723" y="503">tax appeal</text>
        <text class="service" x="723" y="548">asset evaluation</text>
        <text class="service" x="723" y="585">energy audits</text>
      </g>
    </svg>
  </div>

</div>
</body>
</html>
```